Bluefinch Painting needs a Website

We need a website built for a Painting company I own, we mainly do residential painting, but don't want to be limited to that.

Need to have estimate request form.
Need pic's of past projects

I like the look of the website for http://www.harborline-painters.example
& "Thistledown Property inspections"

My logo that was designed here on ArtHive on the front page

I would like one of the houses I downloaded as part of the background
of the front page.

Target Market(s)

Home owners

Industry/Entity Type

Painting

Number of Pages Required

1 page

Font styles to use
Serif

Requirements
Must have
• Estimate request form for home owners to fill out -
• Name:
• Phone Number:
• Address:
• E-mail:
• Painting project description:
• And my info to:
• My phone number: (555) 318-7764
• My web address bluefinchpainting.example
Nice to have
• My logo that was designed here on ArtHive

```html
<!DOCTYPE html>
<html lang="en">
<head>
<meta charset="utf-8">
<title>Bluefinch Painting</title>
<link rel="stylesheet" href="https://fonts.googleapis.com/css2?family=Arimo:wght@400;700&family=Roboto+Slab:wght@400;500&family=Vollkorn:wght@400&display=swap">
<style>
:root{
  --blue:#1f7fc8;
  --blue-dark:#1a6fb0;
  --ink:#222;
  --white:#fff;
  --panel:rgba(40,40,40,.55);
  --field:rgba(235,235,235,.72);
  --dark:#2b2b2b;
}
*{box-sizing:border-box;margin:0;padding:0}
html,body{width:1200px;height:975px;overflow:hidden;background:var(--white)}
body{position:relative;font-family:"Arimo",Arial,sans-serif;color:var(--ink)}
.abs{position:absolute}

/* header */
.brand{left:160px;top:42px;display:flex;align-items:center;gap:12px}
.brand-mark{width:50px;height:50px;background:var(--blue)}
.brand-name{font-family:"Roboto Slab",serif;font-weight:500;font-size:30px;line-height:1;color:var(--blue);letter-spacing:1px;text-transform:uppercase}
.estimate-btn{left:719px;top:17px;width:150px;height:28px;background:var(--blue);color:var(--ink);font-size:17px;display:flex;align-items:center;justify-content:center}
.call{left:884px;top:13px;display:flex;gap:8px;align-items:center}
.call-text small{display:block;font-size:14px;color:#333}
.call-text strong{display:block;font-size:20px;font-weight:400;color:#222}
.nav{left:590px;top:70px;display:flex;list-style:none;font-size:14px}
.nav li{height:25px;display:flex;align-items:center;padding:0 10px;margin-right:10px;color:#222}
.nav li.active{background:var(--blue);color:var(--white);width:64px;justify-content:center;margin-right:10px}

/* hero */
.hero{left:0;top:115px;width:1200px;height:398px;background:linear-gradient(180deg,#8fb0d0 0%,#c9bda3 30%,#b6a98f 55%,#5f7a3e 78%,#3f5b2a 100%)}
.hero-title{left:160px;top:226px;font-family:"Roboto Slab",serif;font-size:32px;line-height:38px;color:var(--white);text-shadow:0 2px 4px rgba(0,0,0,.5);text-transform:uppercase}
.slide-arrow{top:296px;width:40px;height:31px;background:rgba(40,40,40,.75);display:flex;align-items:center;justify-content:center}
.slide-arrow.prev{left:0}.slide-arrow.next{left:1160px}
.quote-panel{left:757px;top:205px;width:285px;height:308px;background:var(--panel)}
.quote-title{left:778px;top:214px;font-family:"Roboto Slab",serif;font-size:21px;color:var(--white)}
.field{left:769px;width:264px;background:var(--field);border-radius:3px;font-size:12px;color:#333;padding:8px 12px}
.submit-row{left:777px;top:472px;width:248px;height:28px}
.submit-btn{left:93px;top:0;width:64px;height:27px;background:#111;color:var(--white);font-weight:700;font-size:14px;display:flex;align-items:center;justify-content:center}
.tab{top:468px;height:45px;font-family:"Roboto Slab",serif;font-size:18px;color:var(--white);display:flex;align-items:center;justify-content:center}
.tab.residential{left:160px;width:245px;background:var(--blue);font-weight:500}
.tab.commercial{left:432px;width:246px;background:var(--dark)}

/* projects */
.thumb{top:548px;width:155px;height:123px;border:1px solid #333;padding:4px;background:var(--white)}
.thumb-img{position:relative;width:100%;height:100%}
.thumb-label{position:absolute;left:0;bottom:0;width:100%;height:28px;background:rgba(40,40,40,.45);color:var(--white);font-family:"Vollkorn",serif;font-size:15px;padding:5px 8px}

/* welcome */
.welcome{left:0;top:689px;width:1200px;height:216px;background:linear-gradient(90deg,#3a3a3a,#4a4a48 45%,#3c3d3a)}
.welcome-title{left:0;top:716px;width:1200px;text-align:center;font-family:"Vollkorn",serif;font-size:22px;color:var(--white)}
.welcome-copy{left:170px;top:776px;width:860px;text-align:center;font-size:12.5px;line-height:22px;color:var(--white)}
.readmore{left:476px;top:856px;width:248px;height:24px}
.readmore-btn{left:85px;top:0;width:78px;height:24px;background:#111;color:var(--white);font-size:13px;display:flex;align-items:center;justify-content:center}

/* footer */
.footer{left:0;top:905px;width:1200px;height:70px;background:var(--blue)}
.foot-nav{left:166px;top:917px;display:flex;list-style:none;font-size:13px;color:var(--white)}
.foot-nav li{margin-right:16px}
.copyright{left:162px;top:939px;font-size:12px;color:var(--white)}
.foot-brand{left:812px;top:922px;display:flex;align-items:center;gap:10px}
.foot-brand .brand-mark{width:34px;height:34px;background:var(--white)}
.foot-brand .brand-name{color:var(--white);font-size:20px}
</style>
</head>
<body>

<header>
  <div class="abs brand"><span class="brand-mark"></span><span class="brand-name">Bluefinch Painting</span></div>
  <div class="abs estimate-btn">Free Estimates</div>
  <div class="abs call">
    <svg width="28" height="28" viewBox="0 0 28 28" aria-hidden="true"><circle cx="14" cy="14" r="12.5" fill="none" stroke="#1f7fc8" stroke-width="2"/><path d="M10 8c-1 1-1 3 0 5 1.5 3 3.5 5 6 6.5 1.5.8 3 .7 4-.3l-2.3-2.3-1.7 1c-1.5-.8-3-2.4-3.8-3.9l1-1.7L11 8z" fill="#1f7fc8"/></svg>
    <div class="call-text"><small>Call Us Today</small><strong>555-318-7764</strong></div>
  </div>
  <ul class="abs nav">
    <li class="active">HOME</li><li>ABOUT US</li><li>SERVICES</li><li>PAST PROJECTS</li><li>CONTACT US</li>
  </ul>
</header>

<section>
  <div class="abs hero" role="img" aria-label="Two-storey beige house with stone entry and flowering garden"></div>
  <h1 class="abs hero-title">Providing quality work at<br>affordable prices</h1>
  <div class="abs slide-arrow prev"><svg width="10" height="12" viewBox="0 0 10 12"><path d="M8 1 2 6l6 5" fill="none" stroke="#fff" stroke-width="2.5"/></svg></div>
  <div class="abs slide-arrow next"><svg width="10" height="12" viewBox="0 0 10 12"><path d="M2 1l6 5-6 5" fill="none" stroke="#fff" stroke-width="2.5"/></svg></div>

  <form class="estimate-form">
    <div class="abs quote-panel"></div>
    <h2 class="abs quote-title">Free Painting Estimates</h2>
    <div class="abs field" style="top:253px;height:28px;padding-top:7px">Name</div>
    <div class="abs field" style="top:298px;height:29px;padding-top:7px">Email</div>
    <div class="abs field" style="top:338px;height:29px;padding-top:7px">Phone</div>
    <div class="abs field" style="top:378px;height:76px">Painting project description</div>
    <div class="abs submit-row">
      <svg class="abs" style="left:0;top:0" width="248" height="28" viewBox="0 0 248 28"><g stroke="#fff" stroke-width="1.5"><line x1="0" y1="14" x2="93" y2="14"/><line x1="70" y1="9" x2="92" y2="9"/><line x1="70" y1="19" x2="92" y2="19"/><line x1="157" y1="14" x2="248" y2="14"/><line x1="157" y1="9" x2="178" y2="9"/><line x1="157" y1="19" x2="178" y2="19"/></g></svg>
      <div class="abs submit-btn">Submit</div>
    </div>
  </form>

  <div class="abs tab residential">RESIDENTIAL PAINTING</div>
  <div class="abs tab commercial">COMMERCIAL PAINTING</div>
</section>

<section class="projects">
  <div class="abs thumb" style="left:175px"><div class="thumb-img" role="img" aria-label="Interior hallway with wood floors and staircase" style="background:linear-gradient(#d8c7a6,#a0724a)"><span class="thumb-label">Lorem Ispum</span></div></div>
  <div class="abs thumb" style="left:348px"><div class="thumb-img" role="img" aria-label="Painter working on white house siding" style="background:linear-gradient(135deg,#1f5fa8,#cfd8e6 55%,#8a949e)"><span class="thumb-label">Lorem Ispum</span></div></div>
  <div class="abs thumb" style="left:521px"><div class="thumb-img" role="img" aria-label="Yellow painted room with white shelves and stairs" style="background:linear-gradient(#e9c24a,#c98a3a)"><span class="thumb-label">Lorem Ispum</span></div></div>
  <div class="abs thumb" style="left:694px"><div class="thumb-img" role="img" aria-label="Large house with green lawn" style="background:linear-gradient(#8fb4d8,#b7ab90 50%,#4f8a33)"><span class="thumb-label">Lorem Ispum</span></div></div>
  <div class="abs thumb" style="left:866px"><div class="thumb-img" role="img" aria-label="Bright entry with white staircase and plant" style="background:linear-gradient(#f1ead8,#c9b58f)"><span class="thumb-label">Lorem Ispum</span></div></div>
</section>

<section>
  <div class="abs welcome" role="img" aria-label="Company work trucks parked in front of a home, darkened"></div>
  <h2 class="abs welcome-title">Welcome to Bluefinch Painting</h2>
  <svg class="abs" style="left:437px;top:748px" width="346" height="16" viewBox="0 0 346 16"><g stroke="#fff" stroke-width="1"><line x1="0" y1="4" x2="346" y2="4"/><line x1="0" y1="7" x2="346" y2="7"/><line x1="168" y1="4" x2="178" y2="14"/><line x1="178" y1="4" x2="168" y2="14"/></g></svg>
  <p class="abs welcome-copy">Lorem ipsum dolor sit amet, consectetuer adipiscing elit, sed diam nonummy nibh euismod&nbsp; rent ut laoreet dolore magna aliquam erat volutpat. Ut wisi enim ad minim veniam, quis nostrud lore xererci tation ullamcorper suscipit lobortis nisl ut aliquip ex ea commodo consequat. Duis autem revel eum iriure dolor in hendrerit in vulputate velit esse molestie consequat.</p>
  <div class="abs readmore">
    <svg class="abs" style="left:0;top:0" width="248" height="24" viewBox="0 0 248 24"><g stroke="#fff" stroke-width="1.5"><line x1="0" y1="12" x2="85" y2="12"/><line x1="70" y1="7" x2="85" y2="7"/><line x1="70" y1="17" x2="85" y2="17"/><line x1="163" y1="12" x2="248" y2="12"/><line x1="163" y1="7" x2="178" y2="7"/><line x1="163" y1="17" x2="178" y2="17"/></g></svg>
    <div class="abs readmore-btn">Read More</div>
  </div>
</section>

<footer>
  <div class="abs footer"></div>
  <ul class="abs foot-nav"><li>• Home</li><li>• About Us</li><li>• Services</li><li>• Past Projects</li><li>• Contact Us</li></ul>
  <p class="abs copyright">Copyright ©2015, BluefinchPainting&nbsp; All Rights Reserved</p>
  <div class="abs foot-brand"><span class="brand-mark"></span><span class="brand-name">Bluefinch Painting</span></div>
</footer>

</body>
</html>
```